Property management company looking for modern card design

We at Blue Heron Partners provides property management services for its residential and commercial properties, with expertise in all categories of multifamily, industrial and office projects throughout California.

We need a business card design that is professional and modern designed business card. In our field, clients get hundreds of business cards, we would like our card to stand out.

Please avoid small print.

Target Market(s)

Professionals and high end clients

Industry/Entity Type

Financial Planning

Contact Information for Business Card

Company Name: Blue Heron Partners, Name, email, license #, phone number, website blueheronpartners.com

Font styles to use
Sans Serif

Requirements
Must have
• The card design needs to be adaptable because there is a possibly we will be expanding into different sectors other than real estate. The card design should be focused on financial planning and asset management.
Nice to have
• Modern and simple business card. Eye catching. Non-standard size/shaped cards would be great.
• blueheronpartners.com
Should not have
• Too many bright color or any pictures or shapes of real estate stuff.

```html
<!DOCTYPE html>
<html lang="en">
<head>
<meta charset="utf-8">
<title>Blue Heron Partners — Business Card</title>
<link rel="stylesheet" href="https://fonts.googleapis.com/css2?family=Lora:wght@400;600&family=Open+Sans:wght@400;600&display=swap">
<style>
  :root {
    --bg: #e4e4e2;
    --card: #ffffff;
    --red: #d71920;
    --red-edge: #b8121a;
    --blush: #f6d9cf;
    --ink: #1e1e1e;
    --muted: #333333;
  }
  * { box-sizing: border-box; margin: 0; padding: 0; }
  html, body { width: 1200px; height: 1021px; overflow: hidden; }
  body {
    background: var(--bg);
    font-family: "Open Sans", sans-serif;
    position: relative;
  }
  .card {
    position: absolute;
    width: 600px;
    height: 343px;
    background: var(--card);
    border-bottom: 10px solid var(--red-edge);
    box-shadow: 0 14px 30px rgba(0,0,0,0.18);
    overflow: hidden;
  }
  .card--front { left: 60px; top: 120px; }
  .card--back  { left: 540px; top: 560px; }

  /* Front */
  .front__mark {
    position: absolute;
    right: 40px; top: 20px;
    width: 260px; height: 260px;
    border-radius: 50%;
    background: var(--blush);
  }
  .front__brand {
    position: absolute;
    right: 30px; top: 120px;
    width: 320px;
    text-align: right;
    font-size: 30px;
    font-weight: 600;
    line-height: 1.1;
    color: var(--red);
  }
  .identity {
    position: absolute;
    left: 40px; top: 120px;
    padding-left: 16px;
    border-left: 8px solid var(--red);
  }
  .identity__name {
    font-family: "Lora", serif;
    font-size: 24px;
    color: var(--ink);
    line-height: 1.1;
  }
  .identity__title {
    font-family: "Lora", serif;
    font-size: 15px;
    color: var(--red);
  }
  .contacts {
    position: absolute;
    left: 40px; bottom: 36px;
    list-style: none;
  }
  .contacts__item {
    display: flex;
    align-items: center;
    gap: 12px;
    font-size: 15px;
    color: var(--muted);
    line-height: 1.7;
  }
  .contacts__icon { width: 14px; height: 14px; fill: var(--red); flex: none; }

  /* Back */
  .back__lockup {
    position: absolute;
    inset: 0;
    display: flex;
    align-items: center;
    justify-content: center;
    gap: 18px;
  }
  .back__dot {
    width: 90px; height: 90px;
    border-radius: 50%;
    background: var(--red);
    flex: none;
  }
  .back__brand {
    font-size: 34px;
    font-weight: 600;
    color: var(--red);
    line-height: 1.1;
  }
</style>
</head>
<body>
  <section class="card card--front">
    <div class="front__mark"></div>
    <div class="front__brand">Blue Heron Partners</div>

    <div class="identity">
      <div class="identity__name">Your Name</div>
      <div class="identity__title">Job Title</div>
    </div>

    <ul class="contacts">
      <li class="contacts__item">
        <svg class="contacts__icon" viewBox="0 0 16 16"><path d="M3 1l3 3-2 2c1 2 3 4 5 5l2-2 3 3-2 3C7 15 1 9 1 3z"/></svg>
        000 000 0000
      </li>
      <li class="contacts__item">
        <svg class="contacts__icon" viewBox="0 0 16 16"><path d="M1 3h14v10H1z M1 3l7 6 7-6" fill="none" stroke="#d71920" stroke-width="1.6"/></svg>
        youremail@xyz.com
      </li>
      <li class="contacts__item">
        <svg class="contacts__icon" viewBox="0 0 16 16"><g fill="none" stroke="#d71920" stroke-width="1.3"><circle cx="8" cy="8" r="6.5"/><ellipse cx="8" cy="8" rx="3" ry="6.5"/><path d="M1.5 8h13"/></g></svg>
        www.blueheronpartners.com
      </li>
    </ul>
  </section>

  <section class="card card--back">
    <div class="back__lockup">
      <div class="back__dot"></div>
      <div class="back__brand">Blue Heron Partners</div>
    </div>
  </section>
</body>
</html>
```